Flyer design for mental health and disability support work company.

The company name 'Harbourlight Disability'

we need a flyer design for our company.

Specialising
Harbourlight Disability is a new KWPS service aimed towards KWPS participants with psychosocial/mental health, intellectual, and cognitive disabilities. We also specialise in supporting participants with a history of being involved in the criminal justice system.

Our focus
Focusing on providing core KWPS supports for community participation, daily activities and supported independent living.

Authentic
Like-minded people passionate about wanting to make a difference in participants' lives.

Our aim is to provide holistic and empowering support targeted towards creating independence and guidance for all participants and families.

Over 35 years of experience working with people with a vast range of disabilities and individual support needs.

Extensive experience not only within KWPS but working with mainstream services within NSW Fairway, Health, Corrections and Parole, Housing, Civic Desk NSW, Pathmark, Brief Assist, QTOB and NSW court systems.

website www.harbourlightdisability.com.au
email for referrals send to - referrals@harbourlightdisability.com.au
for further information send to - hello@harbourlightdisability.com.au

number 1800 372 519

Font styles to use
Serif

Requirements
Should not have
• pictures with people that have disabilities

```html
<!DOCTYPE html>
<html lang="en">
<head>
<meta charset="utf-8">
<title>Harbourlight Disability Flyer</title>
<link href="https://fonts.googleapis.com/css2?family=Mulish:wght@300;400&display=swap" rel="stylesheet">
<style>
  :root {
    --navy: #0f3a5f;
    --gold: #f0b823;
    --sky: #7aa6d8;
    --ink: #1f2a36;
    --paper: #ffffff;
    --backdrop: #e0e0e0;
  }
  * { margin: 0; padding: 0; box-sizing: border-box; }
  html, body {
    width: 1142px; height: 1200px; overflow: hidden;
    background: var(--backdrop);
    font-family: "Mulish", sans-serif;
  }
  .flyer {
    position: absolute; left: 144px; top: 55px;
    width: 857px; height: 1108px;
    background: var(--paper);
    box-shadow: 4px 6px 10px rgba(0,0,0,0.25);
    overflow: hidden;
  }
  .flyer-shapes { position: absolute; left: 0; top: 0; }
  .brand-name {
    position: absolute; left: 571px; top: 136px; width: 180px;
    text-align: center; color: #ffffff;
    font-size: 22px; line-height: 26px; font-weight: 400; letter-spacing: 0.5px;
  }
  .section-title { position: absolute; font-weight: 400; font-size: 27px; line-height: 1.2; }
  .section-text { position: absolute; font-weight: 300; font-size: 16.5px; line-height: 20px; color: var(--ink); }
  .specialising-title { left: 57px; top: 422px; color: #fff; }
  .specialising-text { left: 57px; top: 477px; width: 372px; color: #fff; }
  .focus-title { left: 100px; top: 733px; color: var(--navy); }
  .focus-text { left: 100px; top: 785px; width: 360px; }
  .authentic-title { left: 100px; top: 867px; color: var(--navy); }
  .authentic-text { left: 100px; top: 919px; width: 340px; }
  .aim-text {
    position: absolute; left: 504px; top: 525px; width: 320px;
    color: var(--navy); font-size: 18px; line-height: 22px; font-weight: 400;
  }
  .experience-text { left: 504px; top: 654px; width: 320px; }
  .mainstream-text { left: 504px; top: 735px; width: 320px; }
  .contact-icon { position: absolute; left: 504px; top: 946px; }
  .contact-title { left: 554px; top: 944px; color: var(--gold); font-size: 28px; }
  .contact-list {
    position: absolute; left: 504px; top: 996px; list-style: none;
    color: #fff; font-weight: 300; font-size: 17px; line-height: 22px;
  }
</style>
</head>
<body>
<main class="flyer">
  <svg class="flyer-shapes" width="857" height="1108" viewBox="0 0 857 1108">
    <defs>
      <linearGradient id="photoTone" x1="0" y1="0" x2="1" y2="1">
        <stop offset="0" stop-color="#8a8f94"/>
        <stop offset="0.45" stop-color="#c9a68c"/>
        <stop offset="0.75" stop-color="#6f88b8"/>
        <stop offset="1" stop-color="#2a2e36"/>
      </linearGradient>
    </defs>
    <circle class="feature-disc" cx="231" cy="395" r="276" fill="var(--navy)"/>
    <circle class="photo-ring" cx="184" cy="72" r="332" fill="var(--paper)"/>
    <circle class="photo-frame" cx="184" cy="72" r="320" fill="url(#photoTone)" role="img" aria-label="Photo of two women smiling and holding hands in a warm conversation"/>
    <circle class="brand-disc" cx="661" cy="161" r="114" fill="var(--navy)" stroke="var(--sky)" stroke-width="3"/>
    <path class="contact-panel" d="M376 1094 L465 944 Q520 881 605 881 L857 881 L857 1094 Z" fill="var(--navy)"/>
    <rect class="base-band" x="0" y="1094" width="857" height="14" fill="var(--gold)"/>
  </svg>

  <p class="brand-name">Harbourlight Disability</p>

  <h2 class="section-title specialising-title">Specialising</h2>
  <p class="section-text specialising-text">Harbourlight Disability is a new KWPS service aimed toward KWPS participants with a history of criminal justice, psychosocial/mental health, intellectual, and cognitive disabilities.</p>

  <h2 class="section-title focus-title">Our focus</h2>
  <p class="section-text focus-text">Focusing on providing core KWPS supports for community participation, daily activities and supported independent living.</p>

  <h2 class="section-title authentic-title">Authentic</h2>
  <p class="section-text authentic-text">Likeminded people wanting to make a difference in participant's lives.</p>

  <p class="aim-text">Our aim to provide holistic and empowering supports targeted towards creating independence and guidance for all participants and families.</p>
  <p class="section-text experience-text">Over 35 years of experience working with people that have psychosocial, intellectual, and cognitive disabilities.</p>
  <p class="section-text mainstream-text">Experience in working with mainstream supports under, NSW Fairway, NSW Wellcare, Corrections, Housing, Civic Desk NSW, Pathmark, Brief Assist and Court processes.</p>

  <svg class="contact-icon" width="36" height="34" viewBox="0 0 36 34" fill="none" stroke="var(--gold)" stroke-width="1.8" stroke-linecap="round" stroke-linejoin="round">
    <path d="M4 6 L9 4 L13 11 L10 14 Q13 21 20 25 L23 22 L30 26 L28 31 Q14 32 5 18 Q2 11 4 6 Z"/>
    <rect x="15" y="2" width="19" height="13"/>
    <path d="M15 2 L24.5 9 L34 2"/>
  </svg>
  <h2 class="section-title contact-title">Contact</h2>
  <ul class="contact-list">
    <li>1800 372 519</li>
    <li>www.harbourlightdisability.com.au</li>
    <li>hello@harbourlightdisability.com.au</li>
  </ul>
</main>
</body>
</html>
```